Med Spa business card design with logo

Need a logo design and business card for our new company Velora Skinworks Med Spa. We are a medical office that deals with high end clients. We offer them skin care products which include NERVAX, lip augmentation, and various laser for the skin. I king of like the logo attached, maybe something along those lines but also open to any logo concept.
Updates

Target Market(s)

Out target audience are male and females in the age range of 21-80 years of age

Industry/Entity Type

Medical

Contact Information for Business Card

woukd like front of card to have logo and business name VELORA SKINWORKS MEDSPA. Back of card employee name and phone number along with instagram logo and user name

Font styles to use
Serif
Sans Serif

Requirements
Must have
• prefer monochromatic look white, black, gold
Should not have
• not too colorful

```html
<!DOCTYPE html>
<html lang="en">
<head>
<meta charset="utf-8">
<title>Velora Skinworks Med Spa – Business Card</title>
<link href="https://fonts.googleapis.com/css2?family=Playfair+Display:wght@500&family=Montserrat:wght@400;500&display=swap" rel="stylesheet">
<style>
  :root {
    --backdrop: #efefef;
    --card: #ffffff;
    --card-front: #fafaf8;
    --gold: #d1ad4a;
    --ink: #3a3a3a;
    --shadow: rgba(0, 0, 0, 0.12);
  }
  * { margin: 0; padding: 0; box-sizing: border-box; }
  html, body {
    width: 1200px;
    height: 1000px;
    overflow: hidden;
    background: var(--backdrop);
  }
  .canvas {
    position: relative;
    width: 1200px;
    height: 1000px;
  }
  .card {
    position: absolute;
    width: 540px;
    height: 310px;
    background: var(--card);
    box-shadow: 0 6px 18px var(--shadow);
  }
  .card--front {
    left: 600px;
    top: 190px;
    background: var(--card-front);
    display: flex;
    flex-direction: column;
    align-items: center;
    justify-content: center;
    text-align: center;
  }
  .card--back {
    left: 60px;
    top: 480px;
  }
  .brand-name {
    font-family: "Playfair Display", serif;
    font-weight: 500;
    font-size: 34px;
    letter-spacing: 3px;
    color: var(--gold);
  }
  .brand-tagline {
    margin-top: 8px;
    font-family: "Montserrat", sans-serif;
    font-weight: 500;
    font-size: 12px;
    letter-spacing: 7px;
    color: var(--gold);
  }
  .holder {
    position: absolute;
    left: 0;
    right: 0;
    top: 92px;
    text-align: center;
  }
  .holder-name {
    font-family: "Playfair Display", serif;
    font-weight: 500;
    font-size: 34px;
    letter-spacing: 3px;
    color: var(--ink);
  }
  .holder-role {
    margin-top: 6px;
    font-family: "Montserrat", sans-serif;
    font-weight: 500;
    font-size: 12px;
    letter-spacing: 5px;
    color: var(--ink);
  }
  .contact {
    position: absolute;
    display: flex;
    align-items: center;
    gap: 12px;
    font-family: "Montserrat", sans-serif;
    font-size: 15px;
    letter-spacing: 6px;
    color: var(--ink);
  }
  .contact svg { flex: none; }
  .contact--email { left: 70px; top: 184px; }
  .contact--social { left: 70px; top: 232px; }
  .contact--phone { left: 300px; top: 232px; }
</style>
</head>
<body>
<main class="canvas">
  <section class="card card--front" aria-label="Card front">
    <p class="brand-name">VELORA SKINWORKS</p>
    <p class="brand-tagline">MEDSPA</p>
  </section>

  <section class="card card--back" aria-label="Card back">
    <div class="holder">
      <p class="holder-name">NAME SURNAME</p>
      <p class="holder-role">POSITION</p>
    </div>

    <p class="contact contact--email">
      <svg width="22" height="16" viewBox="0 0 22 16" aria-hidden="true">
        <rect x="0" y="0" width="22" height="16" fill="var(--gold)"/>
        <polyline points="0,0 11,9 22,0" fill="none" stroke="var(--card)" stroke-width="1.5"/>
      </svg>
      email@email.com
    </p>

    <p class="contact contact--social">
      <svg width="18" height="18" viewBox="0 0 18 18" aria-hidden="true">
        <circle cx="9" cy="9" r="9" fill="var(--gold)"/>
      </svg>
      @instagram
    </p>

    <p class="contact contact--phone">
      <svg width="16" height="18" viewBox="0 0 16 18" aria-hidden="true">
        <path d="M3 1 L6 1 L7 5 L5 7 C6 10 8 12 10 13 L12 11 L15 12 L15 15 C15 16 14 17 13 17 C6 16 1 10 1 3 C1 2 2 1 3 1 Z" fill="var(--gold)"/>
      </svg>
      123456789
    </p>
  </section>
</main>
</body>
</html>
```